Packaging & Label Design for CDB Products

We are a European CBD company specialising in athletic recovery, sleep improvement and wellness.

We would like the packaging to incorporate our logo and name (and font 'Codec') 'Lanternfield CBD'. The design must be transferable to all of our products. CBD Oils, Balms, Lip Balm and Vape E-Liquid.

We would like it to be simple but eye-catching and modern. We don't want bright colours. Preferred pallet of muted greys, blacks, white and pastel colours. Geometric concepts, possibly using different colours for each item of the range, we are open to new and fresh ideas (we are seeking you for your experience) and when we find the right design we would likely throw more work in your direction..

Our product range is not complete so the designer must be flexible with some changes and provide files where format can be easily edited by packaging manufacturer. We are also waiting for dimensions for the labels and boxes for several products and will supply the designer with full dimensions of all products once selected.

Oil Box: 2.6 x 9.0 x 2.6 cm (open format 16.7 x 11.6cm)
Labels: 7.8 x 3.3 cm (Front and Back)

Our expected product range will be:
CBD Oil 1000mg
CBD Oil 3000mg
CBD Balm 100mg
CBD Balm 300mg
E-Liquid 500mg
Lip Balm 50mg

We look forward to seeing your ideas.

Best Regards
Lanternfield CBD

```html
<!DOCTYPE html>
<html lang="en">
<head>
<meta charset="utf-8">
<title>Lanternfield CBD – CBD Oil 1000mg packaging</title>
<link rel="stylesheet" href="https://fonts.googleapis.com/css2?family=Barlow+Condensed:wght@500;600;700&family=Montserrat:wght@400;600&display=swap">
<style>
  :root {
    --ink: #3a3a3a;
    --ink-dark: #2f2f2f;
    --mint: #5fcf98;
    --mint-soft: #8fe0b6;
    --paper: #ffffff;
    --backdrop: #f1f2f1;
    --muted: #bcbcbc;
  }
  html, body {
    margin: 0;
    width: 1200px;
    height: 1003px;
    overflow: hidden;
    background: var(--backdrop);
  }
  .canvas {
    position: relative;
    width: 1200px;
    height: 1003px;
  }
  .box-front {
    position: absolute;
    left: 230px;
    top: 70px;
    width: 300px;
    height: 860px;
    box-shadow: 0 10px 30px rgba(0,0,0,0.12);
  }
  .bottle-label {
    position: absolute;
    left: 600px;
    top: 380px;
    width: 540px;
    height: 240px;
    box-shadow: 0 10px 30px rgba(0,0,0,0.12);
  }
  .brand { font-family: "Montserrat", sans-serif; fill: var(--ink); }
  .brand-name { font-weight: 600; letter-spacing: 2px; }
  .brand-sub { font-weight: 400; letter-spacing: 6px; }
  .display { font-family: "Barlow Condensed", sans-serif; font-weight: 700; }
  .display-mid { font-family: "Barlow Condensed", sans-serif; font-weight: 600; }
  .sans { font-family: "Montserrat", sans-serif; }
</style>
</head>
<body>
<main class="canvas">

  <!-- Box front panel -->
  <svg class="box-front" viewBox="0 0 300 860" xmlns="http://www.w3.org/2000/svg">
    <rect width="300" height="860" fill="var(--paper)"/>
    <polygon points="0,580 300,410 300,860 0,860" fill="var(--mint)"/>
    <polygon points="0,600 300,430 300,530 0,700" fill="var(--ink-dark)"/>
    <rect x="0" y="700" width="300" height="52" fill="var(--ink-dark)"/>

    <g class="brand" text-anchor="middle">
      <text class="brand-name" x="150" y="180" font-size="26">LANTERNFIELD</text>
      <line x1="40" y1="205" x2="108" y2="205" stroke="var(--ink)" stroke-width="1.5"/>
      <text class="brand-sub" x="152" y="211" font-size="14">CBD</text>
      <line x1="192" y1="205" x2="260" y2="205" stroke="var(--ink)" stroke-width="1.5"/>
    </g>

    <text class="display" x="22" y="335" font-size="118" fill="var(--ink)">100%</text>
    <text class="display" x="24" y="412" font-size="74" fill="var(--ink)">NATURAL</text>

    <text class="display" x="150" y="592" font-size="84" fill="var(--paper)" text-anchor="middle" transform="rotate(-29.5 150 565)">CBD OIL</text>

    <text class="display-mid" x="285" y="610" font-size="38" fill="var(--paper)" text-anchor="end">1000MG</text>
    <text class="display-mid" x="180" y="686" font-size="22" fill="var(--ink-dark)" text-anchor="middle">LESS THAN 0.3% Δ9 THC</text>
    <text class="sans" x="150" y="735" font-size="22" fill="var(--paper)" text-anchor="middle" letter-spacing="1">FULL SPECTRUM</text>
    <text class="display-mid" x="150" y="805" font-size="26" fill="var(--ink-dark)" text-anchor="middle">1 oz (30ML)</text>
  </svg>

  <!-- Bottle front label -->
  <svg class="bottle-label" viewBox="0 0 540 240" xmlns="http://www.w3.org/2000/svg">
    <rect width="540" height="240" fill="var(--paper)"/>
    <polygon points="70,200 490,90 490,240 70,240" fill="var(--mint)"/>
    <rect x="150" y="168" width="250" height="30" fill="var(--ink-dark)"/>

    <text class="display-mid" x="40" y="120" font-size="16" fill="var(--muted)" text-anchor="middle" transform="rotate(-90 40 120)">LESS THAN 0.3% Δ9 THC</text>
    <text class="sans" x="505" y="120" font-size="14" fill="var(--ink)" text-anchor="middle" transform="rotate(-90 505 120)">www.lanternfieldcbd.com</text>

    <g class="brand" text-anchor="middle">
      <text class="brand-name" x="270" y="38" font-size="17">LANTERNFIELD</text>
      <line x1="200" y1="52" x2="248" y2="52" stroke="var(--ink)" stroke-width="1"/>
      <text class="brand-sub" x="273" y="56" font-size="9">CBD</text>
      <line x1="294" y1="52" x2="342" y2="52" stroke="var(--ink)" stroke-width="1"/>
    </g>

    <text class="display" x="150" y="122" font-size="66" fill="var(--ink-dark)">100%</text>
    <text class="display" x="152" y="160" font-size="40" fill="var(--ink-dark)">NATURAL</text>
    <text class="display-mid" x="394" y="193" font-size="30" fill="var(--paper)" text-anchor="end">CBD OIL</text>
    <text class="display-mid" x="394" y="224" font-size="28" fill="var(--paper)" text-anchor="end">1000MG</text>
    <text class="display-mid" x="150" y="232" font-size="18" fill="var(--ink-dark)">1 oz (30ML)</text>
  </svg>

</main>
</body>
</html>
```